Web site - 5-8 page

We are a small, fresh pasta business called The Noodle Lark located in suburbs of Sacramento, CA. We sell our pasta, ravioli, meatballs and sauce at farmer's markets, events, and soon in our café & marketplace. (Jan 2014) . We also provide catering services. The site needs to communicate FRESH, local, no preservatives, artisan quality pasta. We offer vegetarian, vegan and gluten free products as well.

We would like a web site using our logos and colors to feature what we do, and where people can come buy it. A page to our standard take and make items/menu, our seasonal take and make menu, our catering menu, our new hot food café menu.

We want a page that we can update with "Where can you find The Noodle Lark"
A "specials page" and a page they can order from that they choose the location to pick it up or in the delivery area we deliver to them.
A page with photo's and referrals, testimony, comments, about us, etc. Maybe a page for recipes.
We need to update the events/find us page all the time, weekly, so it needs to be easy for us to go in and do that. We are Window's (not MAC) users if that makes a difference or not, not sure.

Ideally, the same person(s) that make the website would also do a separate project creating our catering and hot food menu brochure/layout and recipe cards

Reason: allow enough time for good quality work

I would like to see the landing page have the pasta shapes/sizes element that is found in the refrigerator wrap, the wrap on the trailer, and the menu - see photo and uploads. It's used as a banner or as a background, bright green.

                                   

 

Would like visitors to be able to "like" me or follow me from my web page. A button or a link?

                                        http://www.brightpantry-example.com/our-food/

Really like the layout of this site. More grocery oriented than café, but we are a take and make marketplace as well as a Panini salads and hot pasta menu for lunch.

Please add Café + Marketplace to headers. Our logo is good but we are now adding a café element and a fresh marketplace, se we need to communicate what we are/what we do. We think adding Café + Marketplace as a descriptor will help. Any ideas, feel free to put your own spin on it. Thank you!!

The designs are good...thanks to everyone!

Reason: To allow for the many updates we have added. Good designs coming in, thank you!

Target Market(s)

#1, busy mom's, busy family's (FAST, Economical meals, no preservatives, local food)
#2 24-34 yr olds that want fresh, vegetarian, vegan or gluten free meal options (no preservatives, local food)
#3 Fresh pasta lovers - any age. The enjoyment of quality fresh pasta and a good meal experience sharing it with friends and family

Industry/Entity Type

Catering

Font styles to use
Other font styles liked:
• EideticNeoRegular, duffy

Colors
9bcb3c
f78f20
eb1f27

Requirements
Must have
• Address, phone, name, logo, colors
Fresh pasta, ravioli, sauce and meatballs in take and make convenient packages. Stress fresh, preservative free, local ingredients, cooks in 45 SECONDS to 3.5 minutes depending on the pasta cut.
FAST meal
Where to find us page - upcoming events
A "specials" page
A page for recipe, how to cook our pasta, how to freeze and store fresh pasta,
How to order online page
Nice to have
• Testimony, links to Facebook, twitter, etc. Place for photo's of product, recent events, customer comments on how they used the product to create their recipe.
Should not have
• No stock photo's of tomato's, no dried pasta images, no Italian flags. No cheesy old world Italian loo or feel. Think fresh, modern, FAST!

```html
<!DOCTYPE html>
<html lang="en">
<head>
<meta charset="utf-8">
<title>The Noodle Lark – Café &amp; Marketplace</title>
<link rel="stylesheet" href="https://fonts.googleapis.com/css2?family=Bungee+Inline&family=Kaushan+Script&family=Merriweather:wght@400&family=Open+Sans:wght@400&family=Raleway:wght@400;500;700&family=Roboto:wght@700&display=swap">
<style>
  :root{
    --green:#9bcb3c;
    --green-band:#c6dc3a;
    --orange:#f78f20;
    --red:#eb1f27;
    --red-bright:#f2321c;
    --yellow:#fcbb12;
    --cream:#faf7ea;
    --ink:#2e2a24;
    --text:#555049;
    --muted:#8a837a;
    --white:#ffffff;
  }
  html,body{margin:0;padding:0;overflow:hidden;background:var(--cream);}
  .page{position:relative;width:1200px;height:1173px;overflow:hidden;background:var(--cream);font-family:'Open Sans',sans-serif;color:var(--ink);}
  .abs{position:absolute;}

  .top-band{left:0;top:0;width:1200px;height:192px;background:var(--green-band);}
  .top-band-edge{left:0;top:192px;width:1200px;height:11px;}

  .brand{left:392px;top:104px;width:400px;text-align:center;font-family:'Raleway',sans-serif;font-weight:700;font-size:40px;line-height:1.1;color:var(--red-bright);}

  .account-links{left:190px;top:226px;display:flex;gap:22px;font-family:'Merriweather',serif;font-size:14px;color:var(--ink);}
  .account-links span{display:flex;align-items:center;gap:8px;}
  .account-links svg{width:26px;height:26px;}

  .phone{left:826px;top:218px;display:flex;align-items:center;gap:8px;font-family:'Merriweather',serif;font-size:24px;color:var(--ink);}
  .phone svg{width:36px;height:40px;}

  .descriptor{left:0;top:334px;width:1200px;text-align:center;font-family:'Bungee Inline',sans-serif;font-size:44px;letter-spacing:2px;color:var(--red-bright);line-height:1;}

  .main-nav{left:159px;top:418px;width:871px;height:71px;display:flex;border:1px solid #b5170f;box-sizing:border-box;background:linear-gradient(var(--orange) 0%,#f05a22 45%,var(--red) 100%);}
  .main-nav a{display:flex;align-items:center;justify-content:center;text-align:center;font-family:'Raleway',sans-serif;font-weight:500;font-size:13.5px;line-height:16px;color:var(--white);text-decoration:none;text-transform:uppercase;border-right:1px solid #c8250f;box-shadow:inset -1px 0 0 rgba(255,255,255,.25);}
  .main-nav a:last-child{border-right:none;box-shadow:none;}

  .slider{left:159px;top:513px;width:871px;height:342px;box-sizing:border-box;border:6px solid var(--orange);background:var(--white);}
  .slide-photo{left:0;top:0;width:549px;height:330px;background:linear-gradient(100deg,#6f5a45 0%,#c9b597 22%,#f1ead8 45%,#e9d39a 60%,#f4f0e6 80%,#ffffff 100%);}
  .slide-art{left:560px;top:8px;width:170px;height:180px;background:linear-gradient(160deg,#fde7e0,#fbf3e3);border-radius:8px;}
  .slide-claim{left:436px;top:200px;width:382px;text-align:center;font-family:'Roboto',sans-serif;font-weight:700;font-size:23px;line-height:26px;color:var(--red);text-transform:uppercase;}
  .slide-arrow{top:127px;width:38px;height:88px;}
  .slide-arrow.prev{left:-6px;}
  .slide-arrow.next{right:-6px;}

  .promise-band{left:159px;top:876px;width:874px;height:83px;}
  .promise-band text{font-family:'Raleway',sans-serif;font-size:22px;fill:var(--white);}

  .find-us{left:159px;top:980px;width:242px;height:89px;background:var(--red-bright);color:var(--white);text-align:center;font-family:'Raleway',sans-serif;box-sizing:border-box;padding-top:14px;}
  .find-us .small{font-size:16px;line-height:18px;}
  .find-us .big{font-size:23px;line-height:27px;}

  .menu-box{left:159px;top:1081px;width:242px;}
  .menu-box h2{margin:0;height:47px;line-height:47px;background:var(--green);text-align:center;font-family:'Raleway',sans-serif;font-weight:400;font-size:27px;color:var(--ink);}
  .menu-box ul{margin:0;padding:0;list-style:none;}
  .menu-box li{height:40px;line-height:40px;padding-left:16px;background:linear-gradient(#f4f4f2,#e3e3e0);border-bottom:1px solid #cfcfcb;font-family:'Merriweather',serif;font-size:16px;color:var(--ink);}
  .menu-box li::before{content:"";display:inline-block;width:9px;height:9px;background:#555;border-radius:2px;margin-right:8px;transform:rotate(45deg) translateY(-2px);}

  .welcome{left:432px;top:983px;width:545px;text-align:center;font-family:'Kaushan Script',cursive;font-size:34px;line-height:46px;white-space:nowrap;}
  .welcome .lead{font-size:25px;color:var(--muted);}
  .welcome .name{color:var(--orange);}
  .divider{left:432px;top:1036px;width:545px;height:14px;}

  .intro{left:432px;top:1056px;width:565px;margin:0;font-size:13.9px;line-height:19.3px;color:var(--text);}
  .read-more{left:922px;top:1163px;font-size:13px;color:var(--red);}
</style>
</head>
<body>
<div class="page">

  <div class="abs top-band" role="img" aria-label="Bright green banner with a pattern of pasta shapes and sizes"></div>
  <svg class="abs top-band-edge" viewBox="0 0 1200 11" preserveAspectRatio="none" aria-hidden="true">
    <defs><pattern id="zigzag" width="15" height="11" patternUnits="userSpaceOnUse"><path d="M0 0H15L7.5 11Z" fill="#c6dc3a"/></pattern></defs>
    <rect width="1200" height="11" fill="url(#zigzag)"/>
  </svg>

  <div class="abs brand">The Noodle Lark</div>

  <div class="abs account-links">
    <span>
      <svg viewBox="0 0 26 26" aria-hidden="true"><circle cx="13" cy="9" r="6" fill="#6b4a3a"/><path d="M2 25c1-7 6-9 11-9s10 2 11 9z" fill="#d8402f"/></svg>
      My Account
    </span>
    <span>
      <svg viewBox="0 0 26 26" aria-hidden="true"><path d="M1 4h4l3 13h13l3-9H7" fill="none" stroke="#e02a20" stroke-width="2.4" stroke-linejoin="round"/><rect x="8" y="9" width="14" height="7" fill="#e02a20"/><circle cx="10" cy="22" r="2.2" fill="#333"/><circle cx="19" cy="22" r="2.2" fill="#333"/></svg>
      My Cart
    </span>
  </div>

  <div class="abs phone">
    <svg viewBox="0 0 36 40" aria-hidden="true"><path d="M9 2c-4 2-6 5-5 10 2 9 8 19 16 24 4 2 7 1 10-2l-6-7-4 2c-4-3-7-9-8-13l4-2z" fill="#d72a1e"/><ellipse cx="22" cy="37" rx="12" ry="2" fill="#bbb"/></svg>
    916.555.0148
  </div>

  <div class="abs descriptor">Café &amp; Marketplace</div>

  <nav class="abs main-nav">
    <a href="#" style="width:84px">Catering<br>Services</a>
    <a href="#" style="width:63px">Cafe<br>Menu</a>
    <a href="#" style="width:66px">Fresh<br>Pasta</a>
    <a href="#" style="width:116px">Marketplace<br>Menu</a>
    <a href="#" style="width:88px">Location<br>Hours</a>
    <a href="#" style="width:75px">Recipes<br>History</a>
    <a href="#" style="width:84px">Blog<br>Archieve</a>
    <a href="#" style="width:82px">Coming<br>Soon</a>
    <a href="#" style="width:63px">Pasta<br>Club</a>
    <a href="#" style="width:70px">Friends<br>Page</a>
    <a href="#" style="width:80px">About<br>Contact</a>
  </nav>

  <div class="abs slider">
    <div class="abs slide-photo" role="img" aria-label="Photo of a plate of fresh spaghetti with peas and ham"></div>
    <div class="abs slide-art" role="img" aria-label="Illustration of the brand character holding a fork and a spoon"></div>
    <div class="abs slide-claim">Fresh, local, no<br>preservatives, artisan quality<br>pasta</div>
    <svg class="abs slide-arrow prev" viewBox="0 0 38 88" aria-hidden="true"><path d="M0 0a44 44 0 0 1 0 88z" fill="#f78f20"/><path d="M16 34l-8 10 8 10" fill="none" stroke="#fff" stroke-width="3.5" stroke-linecap="round" stroke-linejoin="round"/></svg>
    <svg class="abs slide-arrow next" viewBox="0 0 38 88" aria-hidden="true"><path d="M38 0a44 44 0 0 0 0 88z" fill="#f78f20"/><path d="M22 34l8 10-8 10" fill="none" stroke="#fff" stroke-width="3.5" stroke-linecap="round" stroke-linejoin="round"/></svg>
  </div>

  <svg class="abs promise-band" viewBox="0 0 874 83" aria-label="Fresh Pasta, Local Ingredients, Special Sauce, No Preservatives">
    <polygon points="0,0 190,0 230,41.5 190,83 0,83" fill="#fcbb12"/>
    <polygon points="190,0 410,0 450,41.5 410,83 190,83 230,41.5" fill="#f7931f"/>
    <polygon points="410,0 628,0 668,41.5 628,83 410,83 450,41.5" fill="#6fae1e"/>
    <polygon points="628,0 838,0 874,41.5 838,83 628,83 668,41.5" fill="#f2231b"/>
    <text x="108" y="49" text-anchor="middle">Fresh Pasta</text>
    <text x="330" y="49" text-anchor="middle">Local Ingredients</text>
    <text x="548" y="49" text-anchor="middle">Special Sauce</text>
    <text x="758" y="49" text-anchor="middle">No Preservatives</text>
  </svg>

  <div class="abs find-us">
    <div class="small">where can you find</div>
    <div class="big">THE NOODLE LARK</div>
    <div class="small">click here</div>
  </div>

  <div class="abs menu-box">
    <h2>Our Menu</h2>
    <ul><li>Fresh Pasta</li></ul>
  </div>

  <div class="abs welcome"><span class="lead">Welcome to </span><span class="name">The Noodle Lark</span></div>
  <svg class="abs divider" viewBox="0 0 545 14" aria-hidden="true">
    <line x1="0" y1="7" x2="254" y2="7" stroke="#9bcb3c" stroke-width="1"/>
    <line x1="291" y1="7" x2="545" y2="7" stroke="#9bcb3c" stroke-width="1"/>
    <path d="M272.5 12l-5-5a3 3 0 0 1 5-3.5a3 3 0 0 1 5 3.5z" fill="#9bcb3c"/>
  </svg>

  <p class="abs intro">Beciegast nveriti vitaesaert asety kertya aset aplica boserde nerafae kertyuraestyasnemo faserani iasera ptaiadeser daesraeds. Casrolern atur aut oditaut. onsequuntur magni dolqui ratione voluptatemsequi nesciunt orasario numquam eius modi teincidunt, ut labore et dolore magnam lijaseras. Beciegast nveriti vitaesaert asety kertya aset aplica boserde nerafae kertyuraestyasnemo faserani iasera ptaiadeser daesraeds.</p>
  <div class="abs read-more">Read More</div>

</div>
</body>
</html>
```